Lounge Bar Menu

We need an elegant Bar Menu for ou Lounge Bar.
Logo attached.
We already have the support. A cover like a book in A5 format.
Attached as well our menu.

Industry/Entity Type

Bar, Hotel4*

```html
<!DOCTYPE html>
<html lang="fr">
<head>
<meta charset="utf-8">
<title>Velours Lounge Bar – Menu</title>
<link rel="stylesheet" href="https://fonts.googleapis.com/css2?family=Carlito&family=Exo+2:wght@700&display=swap">
<style>
  :root {
    --ink: #000000;
    --royal: #0055ab;
    --paper: #fcfcfc;
    --sheet: #fdfdfd;
    --text: #1a1a1a;
    --white: #ffffff;
  }
  html, body {
    margin: 0;
    width: 1200px;
    height: 1200px;
    overflow: hidden;
    background: var(--sheet);
  }
  .spread {
    position: absolute;
    left: 0; top: 0;
    width: 1932px;
    height: 1932px;
    transform: scale(0.6211);
    transform-origin: 0 0;
  }
  .page {
    position: absolute;
    top: 365px;
    width: 829px;
    height: 1176px;
    overflow: hidden;
  }
  .page svg { position: absolute; inset: 0; width: 100%; height: 100%; }
  .cover { left: 56px; background: var(--ink); }
  .menu-page { left: 1017px; background: var(--paper); }

  .brand-name {
    position: absolute;
    left: 80px;
    top: 150px;
    margin: 0;
    color: var(--white);
    font-family: "Carlito", "Calibri", sans-serif;
    font-weight: 400;
    font-size: 60px;
    line-height: 70px;
    letter-spacing: 2px;
    white-space: nowrap;
  }

  .menu-content {
    position: absolute;
    inset: 0;
    font-family: "Carlito", "Calibri", sans-serif;
    color: var(--text);
    font-size: 16px;
  }
  .menu-content > * { position: absolute; white-space: nowrap; line-height: 22px; margin: 0; }
  .menu-title {
    left: 1331px; width: 200px; top: 428px;
    text-align: center;
    font-family: "Exo 2", sans-serif;
    font-weight: 700;
    font-size: 42px;
    line-height: 46px;
    color: var(--royal);
  }
  .menu-subtitle {
    left: 1330px; width: 200px; top: 513px;
    text-align: center;
    font-size: 20px;
  }
  .section-rule {
    display: flex;
    left: 1051px;
    overflow: hidden;
  }
  .section-rule .dash { flex: 1; overflow: hidden; }
  .section-rule .label { padding: 0 2px; }
  .item { left: 0; width: 1932px; height: 22px; }
  .item > span { position: absolute; top: 0; }
  .item .bullet::before { content: "•"; }
  sup { font-size: 9px; line-height: 0; }
</style>
</head>
<body>
<div class="spread">

  <section class="page cover">
    <svg viewBox="0 0 829 1176" aria-hidden="true">
      <polygon points="829,250 90,700 829,1150" fill="var(--royal)"/>
      <polyline points="829,480 470,700 829,920" fill="none" stroke="var(--white)" stroke-width="28"/>
    </svg>
    <h1 class="brand-name">Velours Lounge Bar</h1>
  </section>

  <section class="page menu-page">
    <svg viewBox="0 0 829 1176" aria-hidden="true">
      <polygon points="680,0 829,0 829,150" fill="var(--royal)"/>
      <polygon points="0,1030 0,1176 150,1176" fill="var(--royal)"/>
    </svg>
  </section>

  <div class="menu-content">
    <h2 class="menu-title">MENU</h2>
    <div class="menu-subtitle">Carte Velours</div>

    <div class="section-rule" style="top:675px; width:733px;">
      <span class="dash">------------------------------------------------------------------------------------------------------------</span>
      <span class="label">A PARTAGER OU PAS</span>
      <span class="dash">------------------------------------------------------------------------------------------------------------</span>
    </div>
    <div style="left:1775px; top:708px;">room</div>

    <div class="item" style="top:742px"><span class="bullet" style="left:1061px"></span><span style="left:1088px">Croque Miura jambon truffé &amp; Reblochon</span><span style="left:1597px">14 €</span><span style="left:1775px">19e</span></div>
    <div class="item" style="top:764px"><span class="bullet" style="left:1061px"></span><span style="left:1088px">Légumes cru, Houmous &amp; Cervelle de Canus</span><span style="left:1604px">7 €</span><span style="left:1782px">12e</span></div>
    <div class="item" style="top:786px"><span class="bullet" style="left:1061px"></span><span style="left:1088px">Rillettes de Sardines au beurre salé &amp; citron vert</span><span style="left:1604px">7 €</span><span style="left:1777px">12</span></div>
    <div class="item" style="top:808px"><span class="bullet" style="left:1061px"></span><span style="left:1088px">planche de Charcuterie de Savoie</span><span style="left:1479px">petite 9 €</span><span style="left:1577px">grande 14€</span><span style="left:1723px">14 et 19</span></div>
    <div class="item" style="top:830px"><span class="bullet" style="left:1061px"></span><span style="left:1088px">Mozzarelle di buffala &amp; tomates cerise</span><span style="left:1601px">11 €</span><span style="left:1775px">16</span></div>
    <div class="item" style="top:852px"><span class="bullet" style="left:1061px"></span><span style="left:1088px">Truite Gravlax, pain taoster &nbsp;&amp; Crème cru</span><span style="left:1649px">14 €</span><span style="left:1781px">19</span></div>

    <div class="section-rule" style="top:971px; width:747px;">
      <span class="dash">------------------------------------------------------------------------------------------------------------</span>
      <span class="label">FROMAGES</span>
      <span class="dash">------------------------------------------------------------------------------------------------------------</span>
    </div>

    <div class="item" style="top:1070px"><span class="bullet" style="left:1077px"></span><span style="left:1104px">Fromages de notre région, mesclun à l’huile de noisette</span><span style="left:1671px">12<sup>e</sup></span><span style="left:1775px">17</span></div>
    <div class="item" style="top:1104px"><span class="bullet" style="left:1077px"></span><span style="left:1104px">Faisselle sucre ou sale</span><span style="left:1675px">7 e</span><span style="left:1775px">9</span></div>

    <div class="section-rule" style="top:1169px; width:751px;">
      <span class="dash">------------------------------------------------------------------------------------------------------------</span>
      <span class="label">DESSERTS</span>
      <span class="dash">------------------------------------------------------------------------------------------------------------</span>
    </div>

    <div class="item" style="top:1236px"><span class="bullet" style="left:1061px"></span><span style="left:1088px">Tarte &nbsp;du jour</span><span style="left:1671px">9 €</span><span style="left:1775px">12</span></div>
    <div class="item" style="top:1291px"><span class="bullet" style="left:1061px"></span><span style="left:1088px">Salade de fruits frais et financier</span><span style="left:1671px">7 €</span><span style="left:1775px">11</span></div>
    <div class="item" style="top:1325px"><span class="bullet" style="left:1061px"></span><span style="left:1088px">Panna cotta coulis de fruits</span><span style="left:1670px">7 e</span><span style="left:1781px">11</span></div>
  </div>

</div>
</body>
</html>
```